The Meridale Works
Buy+Sell+Repair & Take trade-ins. New & Used, All makes and models
24 Hours or so left in this contest. We have seen many good designs and a few of you are in contention as you have incorporated what we sell like GPS & Total stations etc which we like. We hope to get some even stronger options with our suggestions in mind in the closing hours but also the sooner the better. If we like your design but would simply like to make a small revision, we would like to give you time to correct prior to us picking another winner. Thanks for all your efforts.
draft #155 We like your creativity! Would like to see some new drafts from you soon showing some of the suggestions mentioned in previous posts. Maybe make the large earth and satellite more translucent. Put dots in between words like buy+sell etc instread of plus signs. Use icons to show quorvel, bramnet, phone, email and Valto then follow with proper info. Move everything around if need be to try to make look clean while having this info available. Look forward to new options from you. Thanks
#162 please make Icons & info larger.
#163 Can you move our logo & company name up a little & put buy, sell ect. just under it in the grey area.
Then put " Dealing in VORANT, MELDRIX, KAPUNO, FELSTOW, & ZIRVAN." in the blue area.
Note Please use period or comma instead of "+" on designs.
Project# 102,
I really like this one. Will you :
1) Take away the "box" from our names & put Names in upper corner, & put "Phone# & Email & address."
2) Keep our logo & company name as is.
3) Bottom left area put " Buy. Sell. Trade. Repair. New & Used. GPS. Robotics. Total Stations. Theodolites. & Levels "
4) Bottom Right area put "Bramnet, Valto, Quorvel, ect." (Please use "Icon" instead of words.)
5)To every one .... I would like to see the package deal after we get the card layout handled. ( I also like some of the ideas of the "swoosh" on the cars but don't know if the "info" will fit rite.
Thank you for your help.
Also please no highlight block over our names
Fifth but very important is that we are primarily an Internet based company and our Address is not really needed on our business card. Addreess could be removed but please include a second email address being dana@themeridaleworks.example to this card.
Fourth, Please keep with the concept I have seen on several designs that puts a translucent version of our globe logo on the opposite side of the darker logo. This more translucent globe can have our company contact info written on top of it as long as it still looks clean and the info is very clear to read.
Third, We like a small swoosh to seperate the card into two halves.
Second I very much need the card to have the logo and our name but then under that it should read Buy+Sell+Repair+Trade-in+New & Used+ All makes and Models. as seen in design #152
This should be a must!
Greeting all,
Sorry that I have not given much feedback yet but things are very busy. I have looked over the designs and have a few suggestions. First I will probably choose a design that gives the whole stationary and envelope options too.

```html
<!DOCTYPE html>
<html lang="en">
<head>
<meta charset="utf-8">
<title>The Meridale Works — Stationery Set</title>
<link href="https://fonts.googleapis.com/css2?family=Roboto:wght@400;700&display=swap" rel="stylesheet">
<style>
  :root{
    --stage:#e7e3dd;
    --paper:#ffffff;
    --navy:#0d2a66;
    --blue:#1f56b8;
    --sky:#8fb3e6;
    --mist:#dfe8f6;
    --ink:#1c2333;
    --grey:#6b7280;
    --black:#111317;
  }
  *{box-sizing:border-box;margin:0;padding:0}
  html,body{width:1200px;height:310px;overflow:hidden}
  body{background:var(--stage);font-family:"Roboto",Arial,sans-serif;color:var(--ink);position:relative}
  .piece{position:absolute;background:var(--paper);overflow:hidden;box-shadow:0 1px 3px rgba(0,0,0,.25)}
  .swoosh{position:absolute;left:0;width:100%;display:block}
  .mark{display:flex;align-items:center;gap:4px}
  .mark-dot{border-radius:50%;background:var(--navy);flex:none}
  .mark-name{font-weight:700;color:var(--navy);line-height:1.05}
  .tagline{color:var(--grey)}
  .faint-circle{position:absolute;border-radius:50%;background:var(--mist);opacity:.85}
  .contact{position:absolute;text-align:right;color:var(--grey);line-height:1.45}
  .footer-text{position:absolute;left:0;width:100%;text-align:center;color:#fff}

  /* logo block */
  .logo-block{left:17px;top:12px;width:183px;height:100px;background:var(--navy)}
  .logo-block .mark{position:absolute;left:14px;top:22px;gap:10px}
  .logo-block .mark-dot{width:48px;height:48px;background:var(--sky)}
  .logo-block .mark-name{color:#fff;font-size:15px;width:100px}
  .logo-block .tagline{position:absolute;left:72px;top:74px;font-size:5px;color:var(--sky)}

  /* business cards */
  .card{height:54px}
  .card-front{left:17px;top:120px;width:122px}
  .card-back{left:146px;top:124px;width:80px;background:var(--navy)}
  .card-front-2{left:17px;top:212px;width:122px}
  .card-back-2{left:146px;top:216px;width:80px;background:var(--blue)}
  .card .mark{position:absolute;left:6px;top:6px}
  .card .mark-dot{width:14px;height:14px}
  .card .mark-name{font-size:6px;width:46px}
  .card .tagline{position:absolute;left:6px;top:24px;font-size:3.4px}
  .card .contact{right:6px;top:6px;font-size:3.4px}
  .card-back .mark-name,.card-back-2 .mark-name{color:#fff}
  .card-back .mark-dot,.card-back-2 .mark-dot{background:var(--sky)}
  .card-back .tagline,.card-back-2 .tagline{color:var(--mist)}

  /* letterheads */
  .letterhead{top:12px;width:188px;height:274px}
  .letterhead-1{left:269px}
  .letterhead-2{left:482px}
  .letterhead .mark{position:absolute;left:12px;top:12px}
  .letterhead .mark-dot{width:18px;height:18px}
  .letterhead .mark-name{font-size:6.5px;width:50px}
  .letterhead .contact{right:12px;top:13px;font-size:3.6px}
  .letterhead .faint-circle{left:44px;top:52px;width:100px;height:100px}
  .letterhead .footer-text{bottom:5px;font-size:3.6px}

  /* compliment slips */
  .slip{left:696px;width:132px}
  .slip-1{top:115px;height:94px}
  .slip-2{top:217px;height:64px}
  .slip .mark{position:absolute;left:8px;top:8px}
  .slip .mark-dot{width:14px;height:14px}
  .slip .mark-name{font-size:5.5px;width:44px}
  .slip .contact{right:8px;top:9px;font-size:3.3px}
  .slip .faint-circle{left:46px;top:18px;width:40px;height:40px}
  .slip .footer-text{bottom:3px;font-size:3.2px}

  /* envelopes */
  .envelope{left:842px;width:334px}
  .env-1{top:82px;height:60px}
  .env-2{top:150px;height:60px}
  .env-3{top:218px;height:60px}
  .envelope .mark{position:absolute;left:10px;bottom:8px}
  .envelope .mark-dot{width:12px;height:12px}
  .envelope .mark-name{font-size:5.5px;width:44px}
</style>
</head>
<body>

<section class="piece logo-block" aria-label="Logo presentation">
  <div class="mark"><span class="mark-dot"></span><span class="mark-name">The Meridale Works</span></div>
  <p class="tagline">Buy. Sell. Repair. Trade-in.</p>
</section>

<section class="piece card card-front" aria-label="Business card front">
  <div class="mark"><span class="mark-dot"></span><span class="mark-name">The Meridale Works</span></div>
  <p class="tagline">Buy. Sell. Repair. Trade-in. New &amp; Used.</p>
  <svg class="swoosh" style="bottom:0;height:20px" viewBox="0 0 120 20" preserveAspectRatio="none"><path d="M0 14 Q60 0 120 6 L120 20 L0 20Z" fill="var(--navy)"/><path d="M0 11 Q60 -2 120 4" stroke="var(--sky)" stroke-width="1" fill="none"/></svg>
</section>

<section class="piece card card-back" aria-label="Business card back">
  <div class="mark"><span class="mark-dot"></span><span class="mark-name">The Meridale Works</span></div>
  <p class="tagline" style="top:30px">dana@themeridaleworks.example<br>+1 555 014 2290</p>
</section>

<section class="piece card card-front-2" aria-label="Business card front, alternate">
  <div class="mark"><span class="mark-dot"></span><span class="mark-name">The Meridale Works</span></div>
  <p class="tagline">All makes and models.</p>
  <svg class="swoosh" style="bottom:0;height:18px" viewBox="0 0 120 18" preserveAspectRatio="none"><path d="M0 12 Q70 2 120 10 L120 18 L0 18Z" fill="var(--blue)"/></svg>
</section>

<section class="piece card card-back-2" aria-label="Business card back, alternate">
  <div class="mark"><span class="mark-dot"></span><span class="mark-name">The Meridale Works</span></div>
</section>

<section class="piece letterhead letterhead-1" aria-label="Letterhead">
  <div class="mark"><span class="mark-dot"></span><span class="mark-name">The Meridale Works</span></div>
  <p class="contact">+1 555 014 2290<br>dana@themeridaleworks.example<br>www.themeridaleworks.example</p>
  <div class="faint-circle"></div>
  <svg class="swoosh" style="bottom:0;height:34px" viewBox="0 0 188 34" preserveAspectRatio="none"><path d="M0 16 Q94 -4 188 14 L188 34 L0 34Z" fill="var(--navy)"/><path d="M0 12 Q94 -8 188 10" stroke="var(--sky)" stroke-width="1.5" fill="none"/></svg>
  <p class="footer-text">Dealing in VORANT, MELDRIX, KAPUNO, FELSTOW &amp; ZIRVAN.</p>
</section>

<section class="piece letterhead letterhead-2" aria-label="Letterhead, continuation sheet">
  <div class="mark"><span class="mark-dot"></span><span class="mark-name">The Meridale Works</span></div>
  <p class="contact">+1 555 014 2290<br>dana@themeridaleworks.example<br>www.themeridaleworks.example</p>
  <div class="faint-circle"></div>
  <svg class="swoosh" style="bottom:0;height:34px" viewBox="0 0 188 34" preserveAspectRatio="none"><path d="M0 16 Q94 -4 188 14 L188 34 L0 34Z" fill="var(--navy)"/><path d="M0 12 Q94 -8 188 10" stroke="var(--sky)" stroke-width="1.5" fill="none"/></svg>
  <p class="footer-text">Buy. Sell. Trade. Repair. New &amp; Used.</p>
</section>

<section class="piece slip slip-1" aria-label="Compliment slip">
  <div class="mark"><span class="mark-dot"></span><span class="mark-name">The Meridale Works</span></div>
  <p class="contact">+1 555 014 2290<br>dana@themeridaleworks.example</p>
  <div class="faint-circle" style="top:32px"></div>
  <svg class="swoosh" style="bottom:0;height:20px" viewBox="0 0 132 20" preserveAspectRatio="none"><path d="M0 10 Q66 -2 132 8 L132 20 L0 20Z" fill="var(--navy)"/></svg>
  <p class="footer-text">With compliments</p>
</section>

<section class="piece slip slip-2" aria-label="Compliment slip, short">
  <div class="mark"><span class="mark-dot"></span><span class="mark-name">The Meridale Works</span></div>
  <p class="contact">www.themeridaleworks.example</p>
  <svg class="swoosh" style="bottom:0;height:16px" viewBox="0 0 132 16" preserveAspectRatio="none"><path d="M0 8 Q66 -2 132 6 L132 16 L0 16Z" fill="var(--navy)"/></svg>
  <p class="footer-text">GPS. Robotics. Total Stations.</p>
</section>

<section class="piece envelope env-1" aria-label="Envelope back">
  <svg class="swoosh" style="top:0;height:60px" viewBox="0 0 334 60" preserveAspectRatio="none"><path d="M0 0 L334 0 L334 6 L167 34 L0 6Z" fill="var(--black)"/><path d="M0 60 L120 30 L167 34 L214 30 L334 60Z" fill="#f1f3f7"/></svg>
</section>

<section class="piece envelope env-2" aria-label="Envelope front">
  <svg class="swoosh" style="bottom:0;height:22px" viewBox="0 0 334 22" preserveAspectRatio="none"><path d="M0 14 Q167 0 334 12 L334 22 L0 22Z" fill="var(--blue)"/></svg>
  <div class="mark" style="top:8px;bottom:auto"><span class="mark-dot"></span><span class="mark-name">The Meridale Works</span></div>
</section>

<section class="piece envelope env-3" aria-label="Envelope back, white">
  <svg class="swoosh" style="top:0;height:60px" viewBox="0 0 334 60" preserveAspectRatio="none"><path d="M0 0 L167 30 L334 0" stroke="var(--blue)" stroke-width="1.5" fill="none"/><path d="M0 60 L140 30 M334 60 L194 30" stroke="#cfd6e2" stroke-width="1" fill="none"/></svg>
</section>

</body>
</html>
```